Business Card Design

Just looking for a good designs that looks good with our company logo. I'd like it to be simple and to the point. Just including contact information, our logo, and my name somewhere on the card so future clients know who they're contacting, and a couple services offered. The two images I attached are pictures of our logo. I don't care which color they they are, I just attached both images to give a reference of logo colors depending on the color of the card.
Names: Calvin Prewitt
Phone: 555-247-9061
Email: tidyturfcrew@mailvista.net
Services offered:
Mowing
Fertilization
Aeration
Bed & tree maintenance
and more.
Industry/Entity Type
Business
Contact Information for Business Card
Names: Calvin Prewitt
Phone: 555-247-9061
Look and feel

```html
<!DOCTYPE html>
<html lang="en">
<head>
<meta charset="utf-8">
<title>Tidy Turf Crew — Business Card</title>
<link rel="stylesheet" href="https://fonts.googleapis.com/css2?family=Raleway:wght@500;600;700&display=swap">
<style>
  :root {
    --backdrop: #1d1d1f;
    --card: #f7f6f4;
    --accent: #e65a41;
    --navy: #363b48;
    --slate: #5b606c;
    --mist: #c8cbd1;
    --white: #ffffff;
  }
  * { margin: 0; padding: 0; box-sizing: border-box; }
  html, body {
    width: 1200px; height: 871px; overflow: hidden;
    background: var(--backdrop);
    font-family: "Raleway", sans-serif;
  }
  .card {
    position: absolute; left: 110px; top: 155px;
    width: 980px; height: 560px;
    background: var(--card);
    overflow: hidden;
    box-shadow: 0 20px 60px rgba(0,0,0,.6);
  }
  .brand {
    position: absolute; left: 70px; top: 45px;
    width: 270px; height: 270px;
    display: flex; align-items: center; justify-content: center;
  }
  .brand-ring {
    position: absolute; inset: 0;
    border: 14px solid var(--accent);
    border-radius: 50%;
  }
  .brand-name {
    position: relative;
    font-weight: 700; font-size: 38px; line-height: 1.05;
    color: var(--navy); text-align: center; letter-spacing: 1px;
  }
  .holder {
    position: absolute; left: 470px; top: 62px;
    font-size: 44px; font-weight: 600; color: var(--navy);
  }
  .services {
    position: absolute; left: 470px; top: 140px;
    list-style: none;
    font-size: 25px; font-weight: 500; color: var(--navy);
    line-height: 40px;
  }
  .services li::before { content: "- "; }
  .contact-band {
    position: absolute; left: 0; top: 372px;
    width: 100%; height: 86px;
    background: var(--accent);
  }
  .email {
    position: absolute; left: 40px; top: 26px;
    font-size: 26px; font-weight: 500; color: var(--white);
  }
  .icon {
    position: absolute; top: 18px;
    width: 50px; height: 50px;
  }
  .icon-mail { left: 440px; }
  .icon-phone { left: 545px; }
  .phone {
    position: absolute; left: 615px; top: 24px;
    font-size: 30px; font-weight: 600; color: var(--navy);
  }
  .stripe { position: absolute; }
  .stripe-navy { left: 0; top: 458px; width: 600px; height: 22px; background: var(--navy); }
  .stripe-slate { left: 600px; top: 458px; width: 380px; height: 22px; background: var(--slate); }
  .stripe-mist { left: 0; top: 480px; width: 980px; height: 80px; background: var(--mist); }
  .stripe-accent { left: 720px; top: 480px; width: 260px; height: 80px; background: var(--accent); }
</style>
</head>
<body>
  <article class="card">
    <div class="brand">
      <span class="brand-ring"></span>
      <span class="brand-name">TIDY<br>TURF</span>
    </div>

    <h1 class="holder">Calvin Prewitt</h1>
    <ul class="services">
      <li>Mowing</li>
      <li>Fertilization</li>
      <li>Aeration</li>
      <li>Bed &amp; tree maintenance</li>
    </ul>

    <div class="contact-band">
      <span class="email">tidyturfcrew@mailvista.net</span>
      <svg class="icon icon-mail" viewBox="0 0 50 50" aria-hidden="true">
        <rect x="2" y="2" width="46" height="46" rx="10" fill="none" stroke="#363b48" stroke-width="3"/>
        <rect x="12" y="16" width="26" height="18" fill="none" stroke="#363b48" stroke-width="2.5"/>
        <polyline points="12,16 25,27 38,16" fill="none" stroke="#363b48" stroke-width="2.5"/>
      </svg>
      <svg class="icon icon-phone" viewBox="0 0 50 50" aria-hidden="true">
        <rect x="2" y="2" width="46" height="46" rx="10" fill="none" stroke="#363b48" stroke-width="3"/>
        <rect x="17" y="11" width="16" height="28" rx="3" fill="none" stroke="#363b48" stroke-width="2.5"/>
        <line x1="21" y1="33" x2="29" y2="33" stroke="#363b48" stroke-width="2.5"/>
      </svg>
      <span class="phone">555-247-9061</span>
    </div>

    <div class="stripe stripe-navy"></div>
    <div class="stripe stripe-slate"></div>
    <div class="stripe stripe-mist"></div>
    <div class="stripe stripe-accent"></div>
  </article>
</body>
</html>
```